Business cards and stationary for high end Chiropractic wellness center
Harborline Chiropractic Center
Professional
Dr. Tobias K. Feldmore
Board Certified Chiropractor
4382 Elmhaven Ave
Suite 100
Brookvale, PA 17402
care@drfeldmore-example.com
www.harborlineclinic-example.com
Not sure we will have the email on the business cards as we do not like the Doc's personal email on his cards.
The Stationary will not have the Doctor's info only the clinic info
This should be blank
additional color layout

```html
<!DOCTYPE html>
<html lang="en">
<head>
<meta charset="utf-8">
<title>Harborline Chiropractic Center – Business Card</title>
<link href="https://fonts.googleapis.com/css2?family=Montserrat:wght@400;600;700&display=swap" rel="stylesheet">
<style>
  :root {
    --indigo: #2f2a72;
    --indigo-deep: #231f5c;
    --lime: #8cc63f;
    --ink: #3b3b4a;
    --paper: #ffffff;
    --mist: #eef0f2;
    --stage: #e6e7ea;
  }
  * { box-sizing: border-box; margin: 0; padding: 0; }
  html, body { width: 1200px; height: 1009px; overflow: hidden; }
  body {
    background: var(--stage);
    font-family: "Montserrat", sans-serif;
    position: relative;
  }
  .card {
    position: absolute;
    left: 200px;
    width: 800px;
    height: 457px;
    border-radius: 26px;
    overflow: hidden;
    box-shadow: 0 6px 18px rgba(0,0,0,.12);
  }

  /* Front */
  .card-front { top: 30px; background: var(--paper); }
  .accent-square {
    position: absolute; left: 48px; top: 34px;
    width: 78px; height: 44px; background: var(--lime);
  }
  .accent-bar {
    position: absolute; left: 48px; top: 150px; bottom: 0;
    width: 44px; background: var(--indigo);
  }
  .faint-disc {
    position: absolute; right: 40px; top: 140px;
    width: 260px; height: 260px; border-radius: 50%;
    background: var(--mist); opacity: .8;
  }
  .brand {
    position: absolute; left: 150px; top: 48px;
    display: flex; align-items: center; gap: 16px;
  }
  .brand-dot {
    width: 46px; height: 46px; border-radius: 50%; background: var(--lime);
  }
  .brand-name {
    color: var(--indigo); font-weight: 700; font-size: 30px;
    letter-spacing: 1px; line-height: 1.05; text-transform: uppercase;
  }
  .contact {
    position: absolute; left: 126px; top: 166px;
    list-style: none; font-size: 15px; color: var(--ink); line-height: 1.75;
  }
  .contact li { display: flex; align-items: center; gap: 10px; }
  .contact .plain { padding-left: 26px; }
  .contact svg { width: 16px; height: 16px; fill: var(--indigo); flex: none; }
  .doctor {
    position: absolute; right: 60px; bottom: 30px; text-align: right;
  }
  .doctor-name { color: var(--indigo); font-weight: 700; font-size: 26px; }
  .doctor-title { color: var(--lime); font-weight: 600; font-size: 17px; margin-top: 4px; }

  /* Back */
  .card-back {
    top: 522px;
    background: radial-gradient(circle at 55% 45%, var(--indigo) 0%, var(--indigo-deep) 100%);
  }
  .back-brand {
    position: absolute; left: 0; right: 0; top: 150px;
    display: flex; flex-direction: column; align-items: center; gap: 18px;
  }
  .back-dot { width: 96px; height: 96px; border-radius: 50%; background: var(--paper); }
  .back-name {
    color: var(--paper); font-weight: 700; font-size: 28px;
    letter-spacing: 2px; text-transform: uppercase;
  }
  .back-url {
    position: absolute; left: 0; right: 0; bottom: 60px; text-align: center;
    color: var(--lime); font-size: 18px; letter-spacing: 3px;
  }
</style>
</head>
<body>

<section class="card card-front" aria-label="Business card front">
  <div class="faint-disc"></div>
  <div class="accent-square"></div>
  <div class="accent-bar"></div>

  <div class="brand">
    <span class="brand-dot"></span>
    <span class="brand-name">Harborline<br>Chiropractic Center</span>
  </div>

  <ul class="contact">
    <li>
      <svg viewBox="0 0 24 24"><path d="M12 2a7 7 0 0 0-7 7c0 5 7 13 7 13s7-8 7-13a7 7 0 0 0-7-7zm0 9.5A2.5 2.5 0 1 1 12 6.5a2.5 2.5 0 0 1 0 5z"/></svg>
      4382 Elmhaven Ave
    </li>
    <li class="plain">Suite 100</li>
    <li class="plain">Brookvale, PA 17402</li>
    <li>
      <svg viewBox="0 0 24 24"><path d="M6.6 10.8a15 15 0 0 0 6.6 6.6l2.2-2.2a1 1 0 0 1 1-.25 11.4 11.4 0 0 0 3.6.57 1 1 0 0 1 1 1V20a1 1 0 0 1-1 1A17 17 0 0 1 3 4a1 1 0 0 1 1-1h3.5a1 1 0 0 1 1 1c0 1.25.2 2.45.57 3.6a1 1 0 0 1-.25 1z"/></svg>
      717-555-0142
    </li>
    <li>
      <svg viewBox="0 0 24 24"><path d="M6 3h12v5H6zM4 9h16a2 2 0 0 1 2 2v6h-4v4H6v-4H2v-6a2 2 0 0 1 2-2zm4 7v3h8v-3z"/></svg>
      717-555-0143
    </li>
    <li>
      <svg viewBox="0 0 24 24"><path d="M3 5h18v14H3zm2 2v.4l7 4.6 7-4.6V7zm0 2.8V17h14V9.8l-7 4.6z"/></svg>
      care@drfeldmore-example.com
    </li>
    <li>
      <svg viewBox="0 0 24 24"><path d="M12 2a10 10 0 1 0 0 20 10 10 0 0 0 0-20zm6.9 9h-3a15 15 0 0 0-1.3-5.6A8 8 0 0 1 18.9 11zM12 4.1c.9 1.2 1.8 3.7 1.9 6.9h-3.8c.1-3.2 1-5.7 1.9-6.9zM9.4 5.4A15 15 0 0 0 8.1 11h-3a8 8 0 0 1 4.3-5.6zM5.1 13h3a15 15 0 0 0 1.3 5.6A8 8 0 0 1 5.1 13zm6.9 6.9c-.9-1.2-1.8-3.7-1.9-6.9h3.8c-.1 3.2-1 5.7-1.9 6.9zm2.6-1.3a15 15 0 0 0 1.3-5.6h3a8 8 0 0 1-4.3 5.6z"/></svg>
      www.harborlineclinic-example.com
    </li>
  </ul>

  <div class="doctor">
    <p class="doctor-name">Dr. Tobias K. Feldmore</p>
    <p class="doctor-title">Board Certified Chiropractor</p>
  </div>
</section>

<section class="card card-back" aria-label="Business card back">
  <div class="back-brand">
    <span class="back-dot"></span>
    <span class="back-name">Harborline</span>
  </div>
  <p class="back-url">www.harborlineclinic-example.com</p>
</section>

</body>
</html>
```